Pricing Page; Request Quote Page Design

I'm looking to update our pricing page and request page to something more modern in terms of the layout/form design and with more content, but needs to be consistent with the rest of our site. I need two pages designed. 1) A general pricing page w/ CTAs for quotes, and 2) The request quote page with form. Ideally there would be (3) parts for our different packages (Express, Professional, Enterprise) on the pricing page, with CTAs on each section. I like the hero image approach used here https://plovane.com/pricing and here http://www.gridmarrow.com/wp-content/uploads/2016/08/corvalink-pricing-page-design.png In terms of the form page, mainly just looking for an improvement over this https://www.lumadrift.com/price-quote-request

I also included a sample mockup to provide a BIT of guidance, but looking for something a little different and modern.

Industry/Entity Type

Pricing

Number of Pages Required

2 page

Font styles to use
Sans Serif

Requirements
Must have
• Hero background image on main pricing page. Needs to follow the look and feel of lumadrift.com

```html
<!DOCTYPE html>
<html lang="en">
<head>
<meta charset="utf-8">
<title>Pricing — Lumadrift</title>
<link href="https://fonts.googleapis.com/css2?family=Source+Sans+3:wght@300;400;600&display=swap" rel="stylesheet">
<style>
:root{
  --ink:#262626;
  --black:#000;
  --green:#8dc63f;
  --white:#fff;
  --text:#2b2b2b;
  --line:#bdbdbd;
}
*{box-sizing:border-box;margin:0;padding:0}
html,body{width:1200px;height:803px;overflow:hidden}
body{font-family:"Source Sans 3",sans-serif;color:var(--text);background:var(--white);position:relative}
a{text-decoration:none;color:inherit}

.site-header{position:absolute;left:0;top:0;width:1200px;height:116px;background:var(--ink)}
.header-call{position:absolute;left:849px;top:17px;font-size:17px;font-weight:600;color:var(--green)}
.btn{display:inline-flex;align-items:center;justify-content:center;background:var(--green);color:var(--white);font-weight:600;text-transform:uppercase}
.btn-demo{position:absolute;left:1036px;top:13px;width:130px;height:29px;font-size:15px}
.brand{position:absolute;left:27px;top:64px;height:28px;display:flex;align-items:center;color:var(--white);font-size:21px;font-weight:600}
.main-nav{position:absolute;left:445px;top:72px;display:flex;gap:35px;font-size:15px;letter-spacing:1.9px;color:var(--white);text-transform:uppercase}

.hero{position:absolute;left:0;top:116px;width:1200px;height:581px;overflow:hidden}
.hero-image{position:absolute;inset:0;background:
  radial-gradient(ellipse 380px 260px at 380px 300px,rgba(214,170,150,.55),transparent 70%),
  radial-gradient(ellipse 420px 220px at 840px 120px,rgba(190,200,210,.6),transparent 70%),
  linear-gradient(100deg,#c9c7c4 0%,#e6e4e1 35%,#ecebea 60%,#dcdfe2 100%)}
.hero-veil{position:absolute;inset:0;background:rgba(255,255,255,.55)}
.hero-title{position:absolute;left:0;top:60px;width:1200px;text-align:center;font-size:43px;font-weight:300;color:var(--text)}
.hero-lead{position:absolute;left:0;top:126px;width:1200px;text-align:center;font-size:17px;line-height:21px;color:var(--text)}
.hero-lead strong{color:var(--green);font-weight:600}

.plans{position:absolute;left:187px;top:241px;display:flex;gap:18px}
.plan{width:265px;height:273px;background:rgba(255,255,255,.82);border:1px solid var(--line)}
.plan-head{height:97px;background:var(--ink);display:flex;flex-direction:column;align-items:center;padding-top:16px}
.plan-head svg{width:36px;height:36px}
.plan-name{margin-top:2px;font-size:26px;font-weight:600;color:var(--green);letter-spacing:.5px}
.plan-copy{padding:24px 10px 0;height:126px;text-align:center;font-size:13.5px;line-height:20.3px;color:var(--text)}
.plan .btn{display:flex;margin:0 auto;width:147px;height:30px;font-size:15px}

.site-footer{position:absolute;left:0;top:697px;width:1200px;height:106px;background:var(--black)}
.footer-nav{position:absolute;left:53px;top:31px;display:flex;gap:28.5px;font-size:14px;color:var(--white)}
.footer-legal{position:absolute;right:53px;top:35px;font-size:10px;color:var(--white)}
.footer-legal span{color:var(--green);margin:0 4px}
.footer-legal a{color:var(--green)}
</style>
</head>
<body>
<header class="site-header">
  <div class="header-call">CALL 1-866-555-0142</div>
  <a class="btn btn-demo" href="#">Request Demo</a>
  <div class="brand">Lumadrift</div>
  <nav class="main-nav">
    <a href="#">Features</a><a href="#">Services</a><a href="#">Pricing</a><a href="#">Resources</a><a href="#">Blog</a><a href="#">News</a><a href="#">Contact</a>
  </nav>
</header>

<section class="hero">
  <div class="hero-image" role="img" aria-label="Photo of hands typing on a laptop showing analytics charts"></div>
  <div class="hero-veil"></div>
  <h1 class="hero-title">Flexible Pricing Designed to Fit Your Business</h1>
  <p class="hero-lead">Our <strong>pay-as-you-grow</strong> pricing model is geared to minimize risk and maximize return. Whether launching a new learning<br>initiative, or looking to migrate (or integrate) an existing business with our Learning Business Platform, we have you covered.</p>

  <div class="plans">
    <article class="plan">
      <div class="plan-head">
        <svg viewBox="0 0 40 40" fill="none" stroke="#8dc63f" stroke-width="3"><path d="M3 2v35h35"/><path d="M8 31l9-11 6 6 12-15"/><path d="M28 10h8v8" stroke-width="2.5"/></svg>
        <div class="plan-name">EXPRESS</div>
      </div>
      <p class="plan-copy">Launch in weeks, not months. Perfect for smaller businesses with less than 1,000 users and requiring less than 25 courses. Packages start at $499.</p>
      <a class="btn" href="#">Request Quote</a>
    </article>
    <article class="plan">
      <div class="plan-head">
        <svg viewBox="0 0 40 40" fill="none" stroke="#8dc63f" stroke-width="3"><rect x="3" y="11" width="34" height="26" rx="3"/><path d="M13 11V5h14v6"/></svg>
        <div class="plan-name">PROFESSIONAL</div>
      </div>
      <p class="plan-copy">Designed for more established learning businesses which are need to scale and leverage modern technology. Up to 10k users &amp; 100 courses.</p>
      <a class="btn" href="#">Request Quote</a>
    </article>
    <article class="plan">
      <div class="plan-head">
        <svg viewBox="0 0 40 40" fill="none" stroke="#8dc63f" stroke-width="3"><circle cx="20" cy="20" r="17"/><ellipse cx="20" cy="20" rx="7" ry="17"/><path d="M3 20h34M6 11h28M6 29h28"/></svg>
        <div class="plan-name">ENTERPRISE</div>
      </div>
      <p class="plan-copy">For larger organization needing to scale learning globally to more than 10,000 users, with hundreds of courses and multiple instances.</p>
      <a class="btn" href="#">Request Quote</a>
    </article>
  </div>
</section>

<footer class="site-footer">
  <nav class="footer-nav">
    <a href="#">Features</a><a href="#">Services</a><a href="#">Pricing</a><a href="#">Resources</a><a href="#">Blog</a><a href="#">News</a><a href="#">Careers</a><a href="#">Contact</a>
  </nav>
  <div class="footer-legal">Copyright © 2016 Lumadrift, Inc.<span>|</span><a href="#">Privacy Policy</a></div>
</footer>
</body>
</html>
```